KD QUICKSHIFT OIL MENU

I am looking for a new service menu for my oil lube. I need something that stands out and grabs the consumers eye. The size of the menu should be 4' vertical and 8' horizontal. I would like my services to be center on the menu board. I would like for the file to be saved as a .ai file and to be in vector format. I have attached a few files with instructions included. Please feel free to contact me with any questions

Industry/Entity Type

It Service

Colors

Designer to choose colors to be used in the design.

```html
<!DOCTYPE html>
<html lang="en">
<head>
<meta charset="utf-8">
<title>KD Quickshift Oil – Service Menu</title>
<link rel="stylesheet" href="https://fonts.googleapis.com/css2?family=Oswald:wght@500;600;700&family=Roboto+Condensed:ital,wght@0,400;0,700;1,400&family=Kaushan+Script&display=swap">
<style>
:root{
  --green:#0f8a3a;
  --green-dark:#0a6a2b;
  --green-light:#5cc45e;
  --yellow:#f6b81c;
  --yellow-light:#ffd54a;
  --orange:#f39a12;
  --paper:#ececec;
  --paper-light:#f5f5f5;
  --ink:#333;
  --white:#fff;
  --blue:#4ec3ec;
}
*{box-sizing:border-box;margin:0;padding:0}
html,body{width:1200px;height:600px;overflow:hidden;background:var(--white)}
.menu{position:relative;width:1200px;height:600px;overflow:hidden;background:var(--paper);font-family:"Roboto Condensed",Arial,sans-serif;color:var(--ink)}

/* bands */
.check-band{position:absolute;left:0;width:1200px;height:12px;background:linear-gradient(90deg,var(--green-dark),var(--green),var(--green-dark))}
.check-band.top{top:0}
.check-band.bottom{bottom:0;height:22px}
.bottom-stripe{position:absolute;left:0;bottom:22px;width:1200px;height:8px;background:var(--yellow)}

.header{position:absolute;top:12px;left:0;width:1200px;height:62px;background:linear-gradient(180deg,var(--yellow-light),var(--yellow) 60%,var(--orange));border-bottom:3px solid var(--white)}
.brand{position:absolute;top:10px;left:38px;width:318px;height:60px;background:var(--white);border-radius:6px;border:3px solid var(--green);display:flex;align-items:center;justify-content:center;gap:10px;font-family:"Oswald",sans-serif;font-weight:700;font-size:25px;color:var(--green);letter-spacing:.5px}
.brand .dot{width:16px;height:16px;border-radius:50%;background:var(--green)}
.hours{position:absolute;top:22px;left:364px;height:42px;display:flex;align-items:center}
.hours .slot{display:flex;align-items:center;gap:8px;padding:0 12px;height:40px;border-left:1px solid rgba(255,255,255,.7);font-family:"Oswald",sans-serif;color:var(--white)}
.hours .slot:first-child{border-left:none;padding-left:8px}
.hours .day{font-size:12px;font-style:italic;font-weight:600;line-height:12px;text-transform:uppercase}
.hours .time{font-size:19px;font-weight:600}
.hours .time sup{font-size:10px}
.tagline{position:absolute;top:38px;left:880px;width:310px;text-align:center;font-family:"Kaushan Script",cursive;font-size:22px;color:var(--green-dark)}

/* left panel */
.thanks{position:absolute;top:90px;left:40px;width:300px;text-align:center;font-style:italic;font-size:13px}
.wifi{position:absolute;left:-98px;top:320px;width:240px;transform:rotate(-90deg);text-align:center;font-family:"Oswald",sans-serif;font-weight:600;font-size:13px;letter-spacing:3px;color:#bbb}
.oil-card{position:absolute;top:118px;left:42px;width:296px;height:442px;background:var(--paper-light);border-radius:4px;overflow:hidden;box-shadow:0 1px 3px rgba(0,0,0,.15)}
.oil-card .head{position:absolute;top:0;left:0;width:100%;height:96px;background:linear-gradient(135deg,var(--green-light),var(--green))}
.oil-card .t1{position:absolute;top:8px;left:30px;font-family:"Oswald",sans-serif;font-weight:700;font-size:23px;line-height:28px;color:var(--white);transform:rotate(-6deg);transform-origin:left center}
.oil-card .ribbon{position:absolute;top:38px;left:0;width:320px;height:40px;background:var(--yellow);transform:rotate(-6deg);transform-origin:left center;padding-left:32px;font-family:"Oswald",sans-serif;font-weight:700;font-size:30px;line-height:40px;color:var(--white)}
.oil-card .price{position:absolute;top:66px;left:194px;font-family:"Oswald",sans-serif;font-size:19px;line-height:22px;color:var(--white);transform:rotate(-6deg)}
.oil-card .price sup{font-size:11px}
.includes{position:absolute;top:118px;left:24px;font-family:"Oswald",sans-serif;font-weight:700;font-size:16px;letter-spacing:.5px;color:#444}
.checks{position:absolute;top:144px;left:26px;list-style:none}
.checks li{display:flex;align-items:center;gap:7px;font-style:italic;font-size:14px;height:20.8px}
.checks svg{width:14px;height:14px}
.badge{position:absolute;left:210px;width:76px;height:76px;border-radius:50%;background:var(--white);box-shadow:0 0 4px rgba(0,0,0,.12);display:flex;flex-direction:column;align-items:center;justify-content:center;text-align:center;color:#777;font-weight:700;font-size:12px;line-height:13px}
.badge.one{top:182px}.badge.two{top:262px}
.badge .big{font-family:"Oswald",sans-serif;font-size:17px;line-height:18px}
.badge .sm{font-size:8px;font-weight:400}
.car-wash{position:absolute;top:372px;left:26px;width:228px;height:30px;background:var(--blue);clip-path:polygon(0 0,100% 0,96% 50%,100% 100%,0 100%,4% 50%);display:flex;align-items:center;justify-content:center;font-family:"Oswald",sans-serif;font-weight:600;font-size:18px;letter-spacing:1px;color:var(--white)}

/* packages */
.center{position:absolute;top:76px;left:350px;width:510px;height:494px;background:var(--white)}
.package{position:absolute;left:8px;width:495px;overflow:hidden;border-radius:2px;background:linear-gradient(180deg,var(--green-light),var(--green))}
.package.p1{top:19px;height:167px;background:linear-gradient(180deg,var(--green),var(--green-dark))}
.package.p2{top:196px;height:120px}
.package.p3{top:324px;height:88px}
.package.p4{top:420px;height:69px}
.package .tab{position:absolute;top:0;left:0;height:24px;padding:0 44px 0 40px;background:var(--white);clip-path:polygon(0 0,100% 0,90% 100%,8% 100%);font-family:"Oswald",sans-serif;font-weight:600;font-size:14px;color:var(--yellow);line-height:24px}
.package.p3 .tab,.package.p4 .tab{height:18px;line-height:18px;font-size:12px}
.package .extra{position:absolute;top:8px;right:10px;font-size:9px;font-weight:700;color:var(--green-dark)}
.package.p1 .extra{top:18px;right:22px;color:#0a4f20}
.package .dash{position:absolute;top:10px;left:8px;right:8px;bottom:8px;border:1px dashed rgba(0,0,0,.45)}
.items{position:absolute;list-style:none;font-family:"Oswald",sans-serif;font-weight:500;color:var(--white)}
.items li{display:flex;align-items:center;gap:10px}
.items svg{width:28px;height:12px;flex:none}
.p1 .items{top:38px;left:14px;font-size:21px}.p1 .items li{height:29px}
.p2 .items{top:36px;left:20px;font-size:17px}.p2 .items li{height:24px}
.p3 .items{top:28px;left:20px;font-size:15px}.p3 .items li{height:24px}
.p4 .items{top:22px;left:20px;font-size:13px}.p4 .items li{height:20px}
.items .pair{display:flex;gap:18px}
.items .pair span{display:flex;align-items:center;gap:10px}
.band{position:absolute;inset:0;background:linear-gradient(180deg,var(--yellow-light),var(--yellow));clip-path:polygon(64% 100%,100% 34%,100% 100%)}
.deal{position:absolute;transform:rotate(-20deg);color:var(--white);font-family:"Oswald",sans-serif;font-weight:600;text-align:center;white-space:nowrap}
.deal .save{display:block}
.deal .cost{display:block;font-weight:700}
.deal sup{font-size:.5em;vertical-align:top;line-height:1.4}
.p1 .deal{right:18px;bottom:28px}.p1 .deal .save{font-size:19px;line-height:22px}.p1 .deal .cost{font-size:36px;line-height:38px}
.p2 .deal{right:16px;bottom:22px}.p2 .deal .save{font-size:16px;line-height:18px}.p2 .deal .cost{font-size:28px;line-height:30px}
.p3 .deal{right:12px;bottom:18px}.p3 .deal .save{font-size:13px;line-height:15px}.p3 .deal .cost{font-size:22px;line-height:23px}
.p4 .deal{right:10px;bottom:14px}.p4 .deal .save{font-size:11px;line-height:12px}.p4 .deal .cost{font-size:19px;line-height:20px}

/* right panel */
.addons-head{position:absolute;top:88px;left:876px;width:290px;height:32px;background:linear-gradient(180deg,var(--green),var(--green-dark));clip-path:polygon(0 0,100% 0,96% 50%,100% 100%,0 100%);font-family:"Oswald",sans-serif;font-weight:600;font-size:20px;letter-spacing:1px;color:var(--white);line-height:32px;padding-left:34px}
.addons-fold{position:absolute;top:120px;left:1150px;width:16px;height:10px;background:var(--green-dark);clip-path:polygon(0 0,100% 0,0 100%)}
.addons{position:absolute;top:144px;left:888px;width:246px}
.addons h3{font-family:"Oswald",sans-serif;font-weight:600;font-size:15px;line-height:20px;height:20px;color:var(--orange);letter-spacing:.3px;white-space:nowrap}
.addons ul{list-style:none;margin-bottom:6px}
.addons li{display:flex;align-items:baseline;font-size:11px;line-height:14px;height:14.8px;white-space:nowrap}
.addons .maint li{height:15.8px}
.addons li .lead{flex:1;border-bottom:1px dotted #777;margin:0 4px;transform:translateY(-3px)}
.addons li .amt sup{font-size:6px}
</style>
</head>
<body>
<div class="menu">
  <div class="check-band top" role="img" aria-label="Green and white checkered racing band"></div>

  <header class="header"></header>
  <div class="brand"><span class="dot"></span>KD QUICKSHIFT OIL</div>
  <div class="hours">
    <div class="slot"><span class="day">Monday<br>Friday</span><span class="time">8<sup>am</sup>-6<sup>pm</sup></span></div>
    <div class="slot"><span class="day">Saturday</span><span class="time">8<sup>am</sup>-3<sup>pm</sup></span></div>
    <div class="slot"><span class="day">Sunday</span><span class="time">10<sup>am</sup>-3<sup>pm</sup></span></div>
  </div>
  <div class="tagline">More than just an oil change!</div>

  <p class="thanks">"We appreciate Your Business"</p>
  <div class="wifi">FREE WiFi ALWAYS AVAILABLE</div>

  <section class="oil-card">
    <div class="head"></div>
    <div class="t1">FULL SERVICE</div>
    <div class="ribbon">OIL CHANGE</div>
    <div class="price">$31.<sup>95</sup></div>
    <h2 class="includes">INCLUDES</h2>
    <ul class="checks">
      <li><svg viewBox="0 0 14 14"><rect x=".5" y=".5" width="13" height="13" fill="none" stroke="#0f8a3a"/><path d="M3 7l3 3 6-8" fill="none" stroke="#0f8a3a" stroke-width="2"/></svg>Complete Chassis Lubrication</li>
      <li><svg viewBox="0 0 14 14"><rect x=".5" y=".5" width="13" height="13" fill="none" stroke="#0f8a3a"/><path d="M3 7l3 3 6-8" fill="none" stroke="#0f8a3a" stroke-width="2"/></svg>Topoff window wash fluid</li>
      <li><svg viewBox="0 0 14 14"><rect x=".5" y=".5" width="13" height="13" fill="none" stroke="#0f8a3a"/><path d="M3 7l3 3 6-8" fill="none" stroke="#0f8a3a" stroke-width="2"/></svg>Topoff power steering fluid</li>
      <li><svg viewBox="0 0 14 14"><rect x=".5" y=".5" width="13" height="13" fill="none" stroke="#0f8a3a"/><path d="M3 7l3 3 6-8" fill="none" stroke="#0f8a3a" stroke-width="2"/></svg>Check tire pressure</li>
      <li><svg viewBox="0 0 14 14"><rect x=".5" y=".5" width="13" height="13" fill="none" stroke="#0f8a3a"/><path d="M3 7l3 3 6-8" fill="none" stroke="#0f8a3a" stroke-width="2"/></svg>Check air filter</li>
      <li><svg viewBox="0 0 14 14"><rect x=".5" y=".5" width="13" height="13" fill="none" stroke="#0f8a3a"/><path d="M3 7l3 3 6-8" fill="none" stroke="#0f8a3a" stroke-width="2"/></svg>Check wiper blades</li>
      <li><svg viewBox="0 0 14 14"><rect x=".5" y=".5" width="13" height="13" fill="none" stroke="#0f8a3a"/><path d="M3 7l3 3 6-8" fill="none" stroke="#0f8a3a" stroke-width="2"/></svg>Check battery</li>
      <li><svg viewBox="0 0 14 14"><rect x=".5" y=".5" width="13" height="13" fill="none" stroke="#0f8a3a"/><path d="M3 7l3 3 6-8" fill="none" stroke="#0f8a3a" stroke-width="2"/></svg>Check lights</li>
      <li><svg viewBox="0 0 14 14"><rect x=".5" y=".5" width="13" height="13" fill="none" stroke="#0f8a3a"/><path d="M3 7l3 3 6-8" fill="none" stroke="#0f8a3a" stroke-width="2"/></svg>Check belts</li>
    </ul>
    <div class="badge one"><span>change</span><span class="big">OIL</span><span class="sm">upto 5 quarts</span></div>
    <div class="badge two"><span>Install</span><span class="big">NEW</span><span>Oil Filter</span></div>
    <div class="car-wash">FREE CAR WASH</div>
  </section>

  <main class="center">
    <article class="package p1">
      <div class="band"></div>
      <div class="dash"></div>
      <div class="tab">PACKAGE 1</div>
      <div class="extra">High Mileage and Synthetic Oil Additional</div>
      <ul class="items">
        <li><svg viewBox="0 0 28 12"><path d="M0 3h18V0l10 6-10 6V9H0z" fill="#0a5a25"/></svg>Full Service Oil Change</li>
        <li><svg viewBox="0 0 28 12"><path d="M0 3h18V0l10 6-10 6V9H0z" fill="#0a5a25"/></svg>Radiator Flush and Fill</li>
        <li><svg viewBox="0 0 28 12"><path d="M0 3h18V0l10 6-10 6V9H0z" fill="#0a5a25"/></svg>Pair of Wiper Blades</li>
      </ul>
      <div class="deal"><span class="save">Save Over $20</span><span class="cost">$99.<sup>95</sup></span></div>
    </article>

    <article class="package p2">
      <div class="band"></div>
      <div class="tab">PACKAGE 2</div>
      <div class="extra">High Mileage and Synthetic Oil Additional</div>
      <ul class="items">
        <li><svg viewBox="0 0 28 12"><path d="M0 3h18V0l10 6-10 6V9H0z" fill="#0a6a2b"/></svg>Full Service Oil Change</li>
        <li><svg viewBox="0 0 28 12"><path d="M0 3h18V0l10 6-10 6V9H0z" fill="#0a6a2b"/></svg>3 Step Fuel Injector Cleaner</li>
        <li><svg viewBox="0 0 28 12"><path d="M0 3h18V0l10 6-10 6V9H0z" fill="#0a6a2b"/></svg>Pair of Wiper Blades</li>
      </ul>
      <div class="deal"><span class="save">Save Over $20</span><span class="cost">$84.<sup>95</sup></span></div>
    </article>

    <article class="package p3">
      <div class="band"></div>
      <div class="tab">PACKAGE 3</div>
      <div class="extra">High Mileage and Synthetic Oil Additional</div>
      <ul class="items">
        <li><svg viewBox="0 0 28 12"><path d="M0 3h18V0l10 6-10 6V9H0z" fill="#0a6a2b"/></svg>Full Service Oil Change</li>
        <li class="pair"><span><svg viewBox="0 0 28 12"><path d="M0 3h18V0l10 6-10 6V9H0z" fill="#0a6a2b"/></svg>Engine Flush</span><span><svg viewBox="0 0 28 12"><path d="M0 3h18V0l10 6-10 6V9H0z" fill="#0a6a2b"/></svg>Pair of Wiper Blades</span></li>
      </ul>
      <div class="deal"><span class="save">Save Over $20</span><span class="cost">$49.<sup>95</sup></span></div>
    </article>

    <article class="package p4">
      <div class="band"></div>
      <div class="tab">PACKAGE 4</div>
      <div class="extra">High Mileage and Synthetic Oil Additional</div>
      <ul class="items">
        <li class="pair"><span><svg viewBox="0 0 28 12"><path d="M0 3h18V0l10 6-10 6V9H0z" fill="#0a6a2b"/></svg>Full Service Oil Change</span><span><svg viewBox="0 0 28 12"><path d="M0 3h18V0l10 6-10 6V9H0z" fill="#0a6a2b"/></svg>Larkin Oil Stabilizer</span></li>
        <li><svg viewBox="0 0 28 12"><path d="M0 3h18V0l10 6-10 6V9H0z" fill="#0a6a2b"/></svg>Pair of Wiper Blades</li>
      </ul>
      <div class="deal"><span class="save">Save Over $20</span><span class="cost">$49.<sup>95</sup></span></div>
    </article>
  </main>

  <div class="addons-head">ADDITION EXPRESS LUBE</div>
  <div class="addons-fold"></div>
  <section class="addons">
    <h3>PREVENTIVE MAINTENANCE SERVICES</h3>
    <ul class="maint">
      <li>Manual Transmission Fluid Replacement<span class="lead"></span><span class="amt">49.<sup>95</sup></span></li>
      <li>Differently Fluid Exchange<span class="lead"></span><span class="amt">49.<sup>95</sup></span></li>
      <li>Transfer Case Fluid Exchange<span class="lead"></span><span class="amt">159.<sup>95</sup></span></li>
      <li>4X4 Package All Fluid Change<span class="lead"></span><span class="amt">69.<sup>95</sup></span></li>
      <li>Radiator Flush and Fill<span class="lead"></span><span class="amt">49.<sup>95</sup></span></li>
      <li>Flue System Cleaner<span class="lead"></span><span class="amt">19.<sup>95</sup></span></li>
      <li>Engine Flush with any oil change<span class="lead"></span><span class="amt">14.<sup>95</sup></span></li>
      <li>Tire Rotation<span class="lead"></span><span class="amt">16.<sup>95</sup></span></li>
      <li>Air Filter<span class="lead"></span><span class="amt">29.<sup>95</sup></span></li>
      <li>Cabin Air Filter<span class="lead"></span><span class="amt">69.<sup>95</sup></span></li>
      <li>Serpentine Belts<span class="lead"></span><span class="amt">49.<sup>95</sup></span></li>
      <li>Batter Test and Replacement<span class="lead"></span><span class="amt">29.<sup>95</sup></span></li>
      <li>Breaks<span class="lead"></span><span class="amt">79.<sup>95</sup></span></li>
    </ul>
    <h3>VISION AND SAFETY</h3>
    <ul>
      <li>Basic Wiper Blade<span class="lead"></span><span class="amt">9.95</span></li>
      <li>Premium Wiper Blades<span class="lead"></span><span class="amt">12.95</span></li>
      <li>Mini Bulbs<span class="lead"></span><span class="amt">6.95</span></li>
      <li>Headlights<span class="lead"></span><span class="amt">19.95</span></li>
      <li>Headlight Restoration<span class="lead"></span><span class="amt">39.95</span></li>
    </ul>
    <h3>ENGINE TREATMENT AND ADDITIVES</h3>
    <ul>
      <li>Larkin Oil Stabilizer<span class="lead"></span><span class="amt">$14.95</span></li>
      <li>Larkin Oil Stop Leak<span class="lead"></span><span class="amt">$14.95</span></li>
      <li>Larkin Trans Treatment<span class="lead"></span><span class="amt">$14.95</span></li>
      <li>Larkin Fuel System cleaner<span class="lead"></span><span class="amt">$7.95</span></li>
    </ul>
  </section>

  <div class="bottom-stripe"></div>
  <div class="check-band bottom" role="img" aria-label="Green and white checkered racing band"></div>
</div>
</body>
</html>
```